SINGLE PAGE WEBSITE needed for Haunted-House Style Horror Event!

PROJECT:
Single page website to advertise "Bolting Shadows"

ABOUT BOLTING SHADOWS:
Bolting Shadows is a Horror Experience event, that will be held on June 1st 2019 at The Ember Playhouse in Sydney.

At the event, patrons will enter 6 different rooms and have a horror experience in each one.

There's a bar on-site for them to drink as well.

NEEDS FOR THE WEBSITE:
1. Video banner at top, and scrolling photos after video finishes, and text over the top of the video with the name and date of the event
eg.
"A Night of Immersive Horror Experiences"
"The Ember Playhouse | June 1st, 2019"

2. Multiple Book Now buttons on the page, which will link to an external booking platform

3. It should say somewhere "Produced by [MARBLE LANTERN PRODUCTIONS LOGO]"

4. A "Next Steps" section that has the steps for them to complete, such as
- Purchase your ticket HERE for one of our waves
- Rock up at the Ember Playhouse on June 1st at your wave time
- Experience each of our 6 Interactive Horror Rooms
- Grab some drinks at the bar, a bite to eat, and enjoy a fantastic night out!

Other things that should be included somewhere:
- Testimonials
- FAQs (maybe as a dropdown, so it doesn't take up much space?)
- Contact Form on Footer

- - - -

Images, logos, and more attached!

Industry/Entity Type

Events

Coding

Coded - Design and coding required

Number of Pages Required

1 page

Requirements
Nice to have
• 1. Video banner at top, and scrolling photos after video finishes, and text over the top of the video with the name and date of the event
• eg.
• "A Night of Immersive Horror Experiences"
• "The Ember Playhouse | June 1st, 2019"
• 2. multiple Book Now buttons on the page, which will link to an external booking platform
• 3. It should say somewhere "Produced by [Marble Lantern Productions LOGO]" with the Marble Lantern logo
• 4. A "Next Steps" section that has the steps for them to complete, such as
• - Purchase your ticket HERE for one of our waves
• - Rock up at the Ember Playhouse on June 1st at your wave time
• - Experience each of our 6 Interactive Horror Rooms
• - Grab some drinks at the bar, a bite to eat, and enjoy a fantastic night out!
• Other things that should be included somewhere:
• - Testimonials
• - FAQs (maybe as a dropdown, so it doesn't take up much space?)
• - Contact Form on Footer

```html
<!DOCTYPE html>
<html lang="en">
<head>
<meta charset="utf-8">
<title>Bolting Shadows – A Night of Immersive Horror Experiences</title>
<link href="https://fonts.googleapis.com/css2?family=Merienda:wght@700&family=Open+Sans:wght@400;600;700&display=swap" rel="stylesheet">
<style>
:root{
  --bg:#0a0c07;
  --green:#9ccc2f;
  --white:#ffffff;
  --muted:#b9bfae;
  --line:#3a4626;
  --card:#ffffff;
  --ink:#1c1c1c;
}
*{box-sizing:border-box;margin:0;padding:0}
html,body{width:1200px;height:2740px;overflow:hidden;background:var(--bg)}
body{font-family:"Open Sans",Arial,sans-serif;color:var(--white);position:relative}
.heading{font-family:"Merienda",Georgia,serif;font-weight:700}

.page-backdrop{position:absolute;inset:0;background:
  radial-gradient(ellipse 700px 500px at 600px 1350px,#2a3518 0%,transparent 70%),
  radial-gradient(ellipse 600px 400px at 600px 2150px,#1c2510 0%,transparent 70%),
  linear-gradient(#0c0f08,#070905);}

/* header */
.site-header{position:absolute;top:0;left:0;width:1200px;height:72px;display:flex;align-items:center;justify-content:space-between;padding:0 40px 0 24px;z-index:3}
.brand{display:flex;align-items:center;gap:10px;font-weight:700;font-size:19px;color:var(--green);letter-spacing:1px}
.brand-mark{width:18px;height:18px;background:var(--green)}
.main-nav{display:flex;align-items:center;height:72px}
.main-nav a{color:var(--white);text-decoration:none;font-size:12px;font-weight:700;letter-spacing:1px;padding:0 16px;height:72px;line-height:72px}
.main-nav a.active{background:var(--green);color:var(--ink)}
.main-nav a.book{background:var(--green);color:var(--ink);height:34px;line-height:34px;margin-left:14px;border-radius:3px}

/* hero */
.hero{position:absolute;top:0;left:0;width:1200px;height:580px;background:
  radial-gradient(ellipse 420px 260px at 600px 330px,#3c4d1c 0%,#1a2210 55%,#0a0c07 100%);}
.hero-photo{position:absolute;inset:0;background:linear-gradient(180deg,rgba(20,26,12,.2),rgba(10,12,7,.9));}
.hero-title{position:absolute;top:250px;width:1200px;text-align:center;font-size:40px;color:var(--white)}
.hero-date{position:absolute;top:310px;width:1200px;text-align:center;font-size:18px;color:var(--white)}
.play{position:absolute;top:345px;left:570px}
.scroll-hint{position:absolute;top:540px;width:1200px;text-align:center;font-size:9px;letter-spacing:2px;color:var(--muted)}

/* steps */
.section-title{position:absolute;width:1200px;text-align:center;font-size:38px;color:var(--white)}
.steps{position:absolute;top:760px;left:160px;display:flex;gap:22px}
.step{width:206px;height:220px;background:var(--card);border-radius:6px;position:relative;padding:70px 18px 0;text-align:center;color:var(--ink);font-size:14px;line-height:21px;border-bottom:4px solid var(--green)}
.step-num{position:absolute;top:-14px;left:68px;width:70px;height:42px;background:var(--green);color:var(--ink);font-weight:700;font-size:18px;line-height:42px;border-radius:3px}
.btn{display:inline-block;background:var(--green);color:var(--ink);font-weight:700;font-size:12px;letter-spacing:1px;text-decoration:none;border-radius:3px;text-align:center}
.steps-cta{position:absolute;top:1030px;left:544px;width:112px;height:34px;line-height:34px;background:transparent;color:var(--white);border:1px solid var(--white)}

/* testimonials */
.testimonial{position:absolute;top:1230px;display:flex;gap:28px;width:420px}
.avatar{width:130px;height:130px;border-radius:50%;flex:none;background:radial-gradient(circle at 50% 40%,#7a6a55,#2d2118 70%);border:3px solid #d9d2c6}
.avatar.dark{background:radial-gradient(circle at 50% 40%,#555,#111 70%);border-color:#cfcfcf}
.t-name{font-size:20px;color:var(--green);margin-top:6px}
.t-place{font-size:12px;color:var(--green);margin:2px 0 8px}
.t-text{font-size:12px;line-height:18px;color:var(--muted)}
.dots{position:absolute;top:1402px;left:576px;display:flex;gap:10px}
.dots span{width:8px;height:8px;border-radius:50%;background:#6a7355}
.dots span.on{background:var(--green)}

/* faq */
.faq{position:absolute;top:1560px;left:160px;width:888px}
.faq-item{border-bottom:1px solid var(--line);background:rgba(20,26,13,.85)}
.faq-q{display:flex;justify-content:space-between;align-items:center;height:48px;padding:0 18px;font-size:13px;font-weight:600;color:var(--white)}
.faq-q .sign{font-size:22px;font-weight:400;color:var(--white)}
.faq-item.open .faq-q{background:#20291a}
.faq-a{padding:14px 18px 18px;font-size:12px;line-height:19px;color:var(--muted)}

/* contact */
.contact-info{position:absolute;top:2060px;left:160px;width:260px;font-size:12px;line-height:18px;color:var(--muted)}
.info-row{display:flex;gap:14px;margin-bottom:18px;align-items:flex-start}
.contact-form{position:absolute;top:1980px;left:460px;width:588px}
.row{display:flex;gap:20px;margin-bottom:16px}
.field{flex:1;height:40px;border:1px solid var(--line);background:rgba(255,255,255,.03);font-size:12px;color:var(--muted);padding:0 14px;line-height:40px}
.field.message{height:110px;line-height:normal;padding-top:12px}
.send{position:absolute;top:2222px;left:690px;width:130px;height:38px;line-height:38px;border-radius:20px}

/* footer */
.footer-brand{position:absolute;top:2330px;width:1200px;display:flex;justify-content:center}
.footer-brand .brand{font-size:26px}
.footer-brand .brand-mark{width:24px;height:24px}
.social{position:absolute;top:2412px;left:0;width:1200px;display:flex;justify-content:center;gap:26px}
.social span{width:26px;height:26px;border-radius:50%;background:var(--green)}
.produced{position:absolute;top:2488px;width:1200px;text-align:center;font-size:12px;color:var(--muted)}
.producer{position:absolute;top:2512px;left:480px;width:240px;height:70px;border:1px solid #555;display:flex;align-items:center;justify-content:center;text-align:center;font-weight:700;font-size:14px;line-height:18px;color:var(--white);letter-spacing:1px}
.footer-nav{position:absolute;top:2630px;width:1200px;display:flex;justify-content:center}
.footer-nav a{color:var(--white);font-size:11px;font-weight:700;text-decoration:none;padding:8px 16px;letter-spacing:1px}
.footer-nav a.active{background:var(--green);color:var(--ink)}
.copyright{position:absolute;top:2700px;left:0;width:1200px;height:40px;border-top:1px solid var(--line);padding:12px 40px;font-size:10px;color:var(--muted)}
</style>
</head>
<body>
<div class="page-backdrop"></div>

<section class="hero">
  <div class="hero-photo" role="img" aria-label="Dark misty backdrop of a haunted scene behind the event banner"></div>
  <h1 class="heading hero-title">Experience the Best Horror Event</h1>
  <p class="heading hero-date">Held on 1st June 2019</p>
  <svg class="play" width="60" height="60" viewBox="0 0 60 60"><circle cx="30" cy="30" r="27" fill="none" stroke="#fff" stroke-width="3"/><path d="M24 18 L42 30 L24 42 Z" fill="#fff"/></svg>
  <div class="scroll-hint">SCROLL<br><svg width="14" height="8" viewBox="0 0 14 8"><path d="M1 1 L7 7 L13 1" stroke="#b9bfae" fill="none" stroke-width="1.5"/></svg></div>
</section>

<header class="site-header">
  <div class="brand"><span class="brand-mark"></span>BOLTING SHADOWS</div>
  <nav class="main-nav">
    <a class="active" href="#">HOME</a>
    <a href="#">ABOUT</a>
    <a href="#">TESTIMONIALS</a>
    <a href="#">FAQS</a>
    <a href="#">CONTACT</a>
    <a class="book" href="#">BOOK NOW</a>
  </nav>
</header>

<h2 class="heading section-title" style="top:652px">Complete Following Steps &amp; Enjoy Horror Event</h2>
<div class="steps">
  <div class="step"><div class="step-num">01</div>Purchase your ticket HERE for one of our waves</div>
  <div class="step"><div class="step-num">02</div>Rock up at the Ember Playhouse on June 1st at your wave time</div>
  <div class="step"><div class="step-num">03</div>Experience each of our 6 Interactive Horror Rooms</div>
  <div class="step"><div class="step-num">04</div>Grab some drinks at the bar, a bite to eat, and enjoy a fantastic night out!</div>
</div>
<a class="btn steps-cta" href="#">BOOK NOW</a>

<h2 class="heading section-title" style="top:1150px">Testimonials</h2>
<div class="testimonial" style="left:160px">
  <div class="avatar" role="img" aria-label="Portrait photo of guest Tessa Vale"></div>
  <div>
    <div class="heading t-name">Tessa Vale</div>
    <div class="t-place">City, Town</div>
    <p class="t-text">Six rooms of pure dread and I loved every second. The actors never broke character and the bar afterwards was the perfect way to calm my nerves with friends.</p>
  </div>
</div>
<div class="testimonial" style="left:620px">
  <div class="avatar dark" role="img" aria-label="Portrait photo of guest Milo Grant"></div>
  <div>
    <div class="heading t-name">Milo Grant</div>
    <div class="t-place">City, Town</div>
    <p class="t-text">Best night out in Sydney this year. Every room had a new twist, the sets felt real and the scares kept coming until the very last door closed.</p>
  </div>
</div>
<div class="dots"><span class="on"></span><span></span><span></span></div>

<h2 class="heading section-title" style="top:1470px">FAQs</h2>
<div class="faq">
  <div class="faq-item open">
    <div class="faq-q">How long does the whole horror experience take from start to finish? <span class="sign">–</span></div>
    <p class="faq-a">Each wave moves through all six rooms in about forty five minutes. Please arrive fifteen minutes before your wave time so our crew can check your ticket, brief your group and get you ready. After the last room you are welcome to stay on at the bar, grab a bite to eat and share your stories with the rest of the guests for as long as you like.</p>
  </div>
  <div class="faq-item"><div class="faq-q">Is there a minimum age to enter the rooms on the night? <span class="sign">+</span></div></div>
  <div class="faq-item"><div class="faq-q">Can I change my wave time after my ticket has been booked? <span class="sign">+</span></div></div>
  <div class="faq-item"><div class="faq-q">Will the performers touch me inside any of the rooms? <span class="sign">+</span></div></div>
  <div class="faq-item"><div class="faq-q">Is food and drink available at the venue during the event? <span class="sign">+</span></div></div>
</div>

<h2 class="heading section-title" style="top:1985px;width:auto;left:160px;text-align:left">Contact Us</h2>
<div class="contact-info">
  <div class="info-row"><svg width="16" height="20" viewBox="0 0 16 20"><path d="M8 1a6 6 0 0 0-6 6c0 5 6 12 6 12s6-7 6-12a6 6 0 0 0-6-6z" fill="none" stroke="#b9bfae" stroke-width="1.5"/><circle cx="8" cy="7" r="2" fill="#b9bfae"/></svg><span>The Ember Playhouse, 12 Lantern Lane, Sydney NSW 2000</span></div>
  <div class="info-row"><svg width="18" height="14" viewBox="0 0 18 14"><rect x="1" y="1" width="16" height="12" fill="none" stroke="#b9bfae" stroke-width="1.5"/><path d="M1 1 L9 8 L17 1" fill="none" stroke="#b9bfae" stroke-width="1.5"/></svg><span>hello@boltingshadows.com</span></div>
  <div class="info-row"><svg width="16" height="16" viewBox="0 0 16 16"><path d="M3 1 L6 1 L7 5 L5 6 Q6 9 10 11 L11 9 L15 10 L15 13 Q14 15 12 15 Q2 13 1 3 Q1 1 3 1z" fill="none" stroke="#b9bfae" stroke-width="1.3"/></svg><span>(02) 5550 1960</span></div>
</div>
<form class="contact-form">
  <div class="row"><div class="field">First Name</div><div class="field">Last Name</div></div>
  <div class="row"><div class="field">Email</div><div class="field">Phone</div></div>
  <div class="row"><div class="field message">Message</div></div>
</form>
<a class="btn send" href="#">SEND</a>

<div class="footer-brand"><div class="brand"><span class="brand-mark"></span>BOLTING SHADOWS</div></div>
<div class="social"><span></span><span></span><span></span><span></span></div>
<p class="produced">Produced by</p>
<div class="producer">MARBLE LANTERN<br>PRODUCTIONS</div>
<nav class="footer-nav">
  <a class="active" href="#">HOME</a><a href="#">ABOUT</a><a href="#">TESTIMONIALS</a><a href="#">FAQS</a><a href="#">CONTACT</a>
</nav>
<div class="copyright">© Bolting Shadows. All rights reserved.</div>
</body>
</html>
```